Oil and Gas Exploration and Production company needs a business card design

We need a business card design using our logo and colors in the logo. We want a mainstream design.

```html
<!DOCTYPE html>
<html lang="en">
<head>
<meta charset="utf-8">
<title>Korra Oil &amp; Gas — Business Card</title>
<link rel="stylesheet" href="https://fonts.googleapis.com/css2?family=Roboto+Slab:wght@800&family=Arimo:wght@400;700&display=swap">
<style>
  :root {
    --stage: #2b2b2b;
    --card: #ffffff;
    --ink: #0d0d0d;
    --gold: #c99a2e;
    --light-text: #f2f2f2;
  }
  * { box-sizing: border-box; margin: 0; padding: 0; }
  html, body { width: 1200px; height: 880px; overflow: hidden; }
  body {
    background: var(--stage);
    display: flex;
    flex-direction: column;
    align-items: center;
    justify-content: center;
    gap: 56px;
    font-family: "Arimo", Arial, sans-serif;
  }
  .card {
    position: relative;
    width: 620px;
    height: 354px;
    background: var(--card);
    border-radius: 22px;
    overflow: hidden;
  }
  .wordmark {
    display: flex;
    align-items: center;
    gap: 12px;
    font-family: "Roboto Slab", Georgia, serif;
    font-weight: 800;
    color: var(--ink);
    white-space: nowrap;
  }
  .wordmark-dot {
    width: 30px; height: 30px;
    border-radius: 50%;
    background: var(--gold);
    flex: none;
  }
  .card-front .wordmark {
    position: absolute;
    left: 50%; top: 50%;
    transform: translate(-50%, -50%);
    font-size: 44px;
  }
  .card-back .wordmark {
    position: absolute;
    left: 40px; top: 104px;
    font-size: 38px;
  }
  .waves { position: absolute; inset: 0; width: 100%; height: 100%; }
  .holder {
    position: absolute;
    right: 34px; top: 26px;
    text-align: right;
    line-height: 1.1;
  }
  .holder-name { color: var(--gold); font-weight: 700; font-size: 19px; }
  .holder-role { color: var(--ink); font-size: 15px; }
  .contact {
    position: absolute;
    right: 28px; top: 196px;
    text-align: right;
    color: var(--light-text);
    font-size: 13px;
    line-height: 1.32;
    list-style: none;
  }
  .contact-address { margin-bottom: 12px; }
  .contact-line { display: flex; align-items: center; justify-content: flex-end; gap: 8px; }
  .contact-icon { width: 15px; height: 15px; flex: none; }
</style>
</head>
<body>

  <section class="card card-front" aria-label="Card front">
    <div class="wordmark"><span class="wordmark-dot"></span>Korra Oil &amp; Gas</div>
  </section>

  <section class="card card-back" aria-label="Card back">
    <svg class="waves" viewBox="0 0 620 354" preserveAspectRatio="none" aria-hidden="true">
      <path fill="var(--ink)" d="M620 96 C520 100 440 120 412 190 C388 250 360 330 300 354 L620 354 Z"/>
      <path fill="var(--ink)" d="M590 92 C500 104 428 126 400 190 C376 246 340 320 240 354 L0 354 L0 344 C170 338 340 310 380 200 C404 140 480 106 590 92 Z"/>
      <path fill="var(--gold)" d="M0 312 C180 306 290 270 330 190 C320 262 250 318 0 330 Z"/>
    </svg>

    <div class="wordmark"><span class="wordmark-dot"></span>Korra Oil &amp; Gas</div>

    <div class="holder">
      <p class="holder-name">Mara Velden</p>
      <p class="holder-role">President &amp; CEO</p>
    </div>

    <ul class="contact">
      <li class="contact-address">PO Box 480, Harbor Road<br>4th Lane, Leeds</li>
      <li class="contact-line">+01 5550 0142
        <svg class="contact-icon" viewBox="0 0 16 16" aria-hidden="true"><circle cx="8" cy="8" r="8" fill="var(--gold)"/><path d="M5 4.5h2l.6 2-1 .8c.5 1 1.2 1.7 2.1 2.1l.8-1 2 .6v2c-3.7.3-6.8-2.8-6.5-6.5z" fill="var(--ink)"/></svg>
      </li>
      <li class="contact-line">hello@korraoil.com
        <svg class="contact-icon" viewBox="0 0 16 16" aria-hidden="true"><circle cx="8" cy="8" r="8" fill="var(--gold)"/><rect x="4" y="5" width="8" height="6" fill="var(--ink)"/><path d="M4 5l4 3.2L12 5" stroke="var(--gold)" stroke-width="1" fill="none"/></svg>
      </li>
      <li class="contact-line">www.korraoil.com
        <svg class="contact-icon" viewBox="0 0 16 16" aria-hidden="true"><circle cx="8" cy="8" r="8" fill="var(--gold)"/><circle cx="8" cy="8" r="4.2" fill="none" stroke="var(--ink)" stroke-width="1.1"/><ellipse cx="8" cy="8" rx="1.8" ry="4.2" fill="none" stroke="var(--ink)" stroke-width="1"/><path d="M3.8 8h8.4" stroke="var(--ink)" stroke-width="1"/></svg>
      </li>
    </ul>
  </section>

</body>
</html>
```